Hello again

I have a few Logos I am looking to add

Target Market(s)

MediSpa

Industry/Entity Type

Medispa

Contact Information for Business Card

Dana Whitcombe, Owner/Medical Aesthetician, 587-555-0142, Unit 214 - 1450 17 Ave NW, T3K 5P9 Calgary, AB., www.GlowNestSpa.ca ....QR codes are attached I do really like the former business card but everything was in teal, gold and white.

```html
<!DOCTYPE html>
<html lang="en">
<head>
<meta charset="utf-8">
<title>GlowNest MediSpa – Business Card</title>
<link href="https://fonts.googleapis.com/css2?family=Poppins:wght@400;500&family=Allura&display=swap" rel="stylesheet">
<style>
  :root {
    --bg: #e6e6e6;
    --card: #050505;
    --gold: #d2b45a;
    --gold-deep: #b8983f;
    --white: #f4f4f4;
    --divider: #1a1a1a;
  }
  * { box-sizing: border-box; margin: 0; padding: 0; }
  html, body { width: 1200px; height: 1200px; overflow: hidden; }
  body {
    background: var(--bg);
    font-family: "Poppins", Arial, sans-serif;
    position: relative;
  }
  .card {
    position: absolute;
    background: var(--card);
  }
  .card--front {
    left: 406px; top: 50px; width: 386px; height: 674px;
    text-align: center;
    color: var(--white);
  }
  .card--back {
    left: 251px; top: 754px; width: 695px; height: 395px;
    display: flex; align-items: center; justify-content: center;
  }
  .brand {
    display: flex; flex-direction: column; align-items: center;
  }
  .brand__row { display: flex; align-items: center; gap: 10px; }
  .brand__dot {
    width: 14px; height: 14px; border-radius: 50%;
    background: var(--gold);
  }
  .brand__name {
    font-family: "Poppins", Arial, sans-serif;
    font-weight: 500;
    color: var(--gold);
    letter-spacing: 0.5px;
    white-space: nowrap;
  }
  .brand__tagline {
    color: var(--gold);
    font-weight: 500;
    text-transform: uppercase;
    letter-spacing: 2px;
    white-space: nowrap;
  }
  .card--front .brand { margin-top: 62px; }
  .card--front .brand__name { font-size: 30px; }
  .card--front .brand__tagline { font-size: 9px; margin-top: 4px; }
  .card--back .brand__name { font-size: 56px; }
  .card--back .brand__dot { width: 24px; height: 24px; }
  .card--back .brand__tagline { font-size: 14px; margin-top: 6px; letter-spacing: 3px; }

  .person__name {
    font-family: "Allura", cursive;
    color: var(--gold);
    font-size: 56px;
    line-height: 1;
    margin-top: 168px;
  }
  .person__role {
    font-size: 17px;
    margin-top: 12px;
    letter-spacing: 0.2px;
  }
  .contact-icons {
    display: block;
    margin: 34px auto 0;
  }
  .contact {
    margin-top: 30px;
    font-size: 17px;
    line-height: 28px;
  }
  .contact__web {
    display: block;
    color: var(--gold);
    font-weight: 500;
    font-size: 17px;
    letter-spacing: 1px;
    margin-top: 22px;
  }
</style>
</head>
<body>

  <section class="card card--front">
    <div class="brand">
      <div class="brand__row">
        <span class="brand__dot"></span>
        <span class="brand__name">GlowNest MediSpa</span>
      </div>
      <span class="brand__tagline">Skin &amp; Laser Specialists</span>
    </div>

    <h1 class="person__name">Dana Whitcombe</h1>
    <p class="person__role">Owner/Medical Aesthetician</p>

    <svg class="contact-icons" width="140" height="36" viewBox="0 0 140 36" aria-label="Phone, location and web">
      <rect x="0" y="0" width="140" height="36" rx="18" fill="var(--gold)"/>
      <line x1="50" y1="9" x2="50" y2="27" stroke="var(--divider)" stroke-width="1.4"/>
      <line x1="90" y1="9" x2="90" y2="27" stroke="var(--divider)" stroke-width="1.4"/>
      <!-- phone -->
      <path d="M24 11c-1 0-2 1-2 2 0 7 5 12 12 12 1 0 2-1 2-2l-.5-2.5-3-1-1.5 1.5c-2-1-3.5-2.5-4.5-4.5L28 15l-1-3z" fill="none" stroke="var(--divider)" stroke-width="1.6" stroke-linejoin="round"/>
      <!-- pin -->
      <path d="M70 27c-4-5-6-8-6-11a6 6 0 0 1 12 0c0 3-2 6-6 11z" fill="var(--divider)"/>
      <circle cx="70" cy="16" r="2.2" fill="var(--gold)"/>
      <!-- globe -->
      <g fill="none" stroke="var(--divider)" stroke-width="1.4">
        <circle cx="112" cy="18" r="8"/>
        <ellipse cx="112" cy="18" rx="3.5" ry="8"/>
        <line x1="104" y1="18" x2="120" y2="18"/>
        <line x1="105.5" y1="13.5" x2="118.5" y2="13.5"/>
        <line x1="105.5" y1="22.5" x2="118.5" y2="22.5"/>
      </g>
    </svg>

    <address class="contact" style="font-style:normal">
      587-555-0142<br>
      Unit 214 - 1450 17 Ave NW,<br>
      T3K 5P9 Calgary, AB.
      <span class="contact__web">www.GlowNestSpa.ca</span>
    </address>
  </section>

  <section class="card card--back">
    <div class="brand">
      <div class="brand__row">
        <span class="brand__dot"></span>
        <span class="brand__name">GlowNest MediSpa</span>
      </div>
      <span class="brand__tagline">Skin &amp; Laser Specialists</span>
    </div>
  </section>

</body>
</html>
```